Postcard Design -- Harbor Bridgeworks

Harbor Bridgeworks believes that when low-income immigrants acquire the right tools (skills and abilities), they can overcome poverty and build a pathway to success as new Americans. We accomplish this through our wraparound strategy, which offers a full range of services designed to help people overcome barriers to the acquisition of the skills and abilities they need to thrive. This process involves recognizing the diverse skills immigrants already possess, resolving immediate needs or problems, identifying opportunities for growth, and monitoring progress toward goals. As a result, clients are able to acquire the skills and abilities they need to thrive as new Americans.

We need a postcard design that follows the Harbor Bridgeworks brand, but also has a heartwarming/holiday feel to it with a cool factor. This postcard will be mailed as an insert with our appeal letter. The purpose of this postcard is to encourage donors who receive it to reuse/mail it to someone else and encourage them to donate to Harbor Bridgeworks.

Target Market(s)

Donors

Industry/Entity Type

Non-Profit

Font styles to use
Sans Serif

Requirements
Must have
• Our Colors: #3276b5 #9bcb3c #fece3e #f04a50
• Double sided Postcard:
• Front side:
• - A design that is welcoming and has a heartwarming/holiday feel to it
• - Our logo
• - and a message (examples: 'Thinking About You'.. 'Giving back to the community'.. 'Celebrate with us'.. 'Sharing the holiday spirit'.. 'Share the cheer'.. 'Invest in our community'..) I'm open to new ideas.
• Back side:
• - Mission Statement
• - We help low-income, Spanish-speaking immigrants acquire the tools they need to thrive.
• - Logo
• - site link (harborbridgeworks.org)
• - donation link (donate.harborbridgeworks.org)
• - Call to action (Invest in Harbor Bridgeworks Today!.. Wishing you Happy Holidays, join me in supporting New-Americans today.. etc)
• - Leave area available for sender info and person receiving info (like a regular postcard)
• - 5087310925
• -FB and Twitter icon
Nice to have
• Postcard Final Dimension: 3.5"x5" (with bleed, PLEASE)
• PROJECT SPECIFICS
• Audience = Donors
• Message = Asking other to invest on Harbor Bridgeworks
• Product = Postcard Design 3.5"x5"
• Font = Sans Serif

```html
<!DOCTYPE html>
<html lang="en">
<head>
<meta charset="utf-8">
<title>Harbor Bridgeworks Holiday Postcard</title>
<link href="https://fonts.googleapis.com/css2?family=Arimo:wght@400;700&family=Crimson+Text:ital@1&display=swap" rel="stylesheet">
<style>
  :root {
    --bg: #d9d6cc;
    --card: #ffffff;
    --lavender: #ddd8ec;
    --lavender-soft: #ebe8f4;
    --band: #d3cde6;
    --ink: #222222;
    --muted: #555555;
    --rule: #8a8a8a;
    --brand-blue: #1c79b8;
    --white: #ffffff;
  }
  * { margin: 0; padding: 0; box-sizing: border-box; }
  html, body { width: 1200px; height: 1200px; overflow: hidden; }
  body { background: var(--bg); font-family: "Arimo", Arial, sans-serif; color: var(--ink); position: relative; }

  .postcard { position: absolute; left: 270px; width: 666px; height: 466px; background: var(--card); overflow: hidden; }
  .postcard--front { top: 116px; }
  .postcard--back { top: 648px; }

  /* Front */
  .front-photo { position: absolute; inset: 0; background: linear-gradient(160deg, #b9c9a4 0%, #8fae7c 35%, #a4b9c8 60%, #c98a6f 80%, #7d98b7 100%); }
  .front-band { position: absolute; left: 0; top: 0; width: 100%; height: 45px; background: rgba(221, 216, 236, 0.85); }
  .front-message { position: absolute; left: 56px; top: 8px; font-family: "Crimson Text", Georgia, serif; font-style: italic; font-size: 24px; color: var(--white); }
  .front-sign { position: absolute; right: 42px; bottom: 22px; display: flex; align-items: center; gap: 6px; color: var(--white); font-size: 13px; }
  .front-sign .mark { width: 14px; height: 14px; background: var(--white); }

  /* Back */
  .back-decor { position: absolute; left: 0; bottom: 0; width: 340px; height: 200px; background: radial-gradient(ellipse at 40% 70%, var(--lavender) 0%, var(--lavender-soft) 55%, rgba(255,255,255,0) 80%); }
  .back-decor--top { left: 200px; top: 0; bottom: auto; width: 180px; height: 120px; background: radial-gradient(ellipse at 50% 20%, var(--lavender-soft) 0%, rgba(255,255,255,0) 70%); }
  .brand { position: absolute; left: 58px; top: 50px; display: flex; align-items: center; gap: 7px; font-size: 16px; font-weight: 700; color: var(--brand-blue); }
  .brand .mark { width: 16px; height: 16px; background: var(--brand-blue); }
  .greeting { position: absolute; left: 58px; top: 138px; font-family: "Crimson Text", Georgia, serif; font-style: italic; font-size: 21px; }
  .appeal { position: absolute; left: 58px; top: 182px; width: 270px; font-size: 14px; line-height: 18px; }
  .links { position: absolute; left: 0; top: 222px; width: 328px; height: 58px; background: var(--band); padding: 10px 0 0 58px; font-family: "Crimson Text", Georgia, serif; font-style: italic; font-size: 15.5px; line-height: 20px; color: var(--white); }
  .contact { position: absolute; left: 58px; top: 328px; list-style: none; font-size: 12.5px; line-height: 16px; }
  .contact li { display: flex; gap: 5px; }
  .contact svg { width: 10px; height: 10px; margin-top: 2px; flex: none; }
  .contact .dot { width: 9px; height: 9px; border-radius: 50%; background: var(--ink); margin-top: 3px; flex: none; }
  .divider { position: absolute; left: 342px; top: 48px; width: 1px; height: 388px; background: var(--rule); }
  .stamp { position: absolute; left: 515px; top: 44px; width: 109px; height: 124px; border: 1px solid #bbbbbb; }
  .field-label { position: absolute; left: 359px; font-size: 10.5px; color: var(--muted); }
  .address-line { position: absolute; left: 359px; width: 265px; height: 1px; background: var(--rule); }
</style>
</head>
<body>
  <section class="postcard postcard--front">
    <div class="front-photo" role="img" aria-label="Photograph of a smiling family of four outdoors in a park, with soft white snowflake decorations"></div>
    <div class="front-band"></div>
    <p class="front-message">Thinking about you</p>
    <div class="front-sign"><span class="mark"></span><span>Harbor Bridgeworks | 2015</span></div>
  </section>

  <section class="postcard postcard--back">
    <div class="back-decor" role="img" aria-label="Faint lavender snowflake decoration"></div>
    <div class="back-decor back-decor--top" role="img" aria-label="Faint lavender snowflake decoration"></div>
    <div class="brand"><span class="mark"></span><span>Harbor Bridgeworks</span></div>
    <p class="greeting">Wishing you a Happy Holidays</p>
    <p class="appeal">Join me in supporting New-Americans today...</p>
    <div class="links">
      <p>Site: www.harborbridgeworks.org</p>
      <p>Invest: www.donate.harborbridgeworks.org</p>
    </div>
    <ul class="contact">
      <li><svg viewBox="0 0 10 10"><path d="M2 0.5 L3.8 2.6 L2.8 3.8 Q4 6.2 6.2 7.2 L7.4 6.2 L9.5 8 L8 9.6 Q3.5 9 0.4 2 Z" fill="#222"/></svg><span>508 731 0925</span></li>
      <li><span class="dot"></span><span>/harborbridgeworks.Harborview</span></li>
      <li><span class="dot"></span><span>/harborbridgeworks</span></li>
      <li><svg viewBox="0 0 10 10"><path d="M5 10 L1.6 4.6 A3.6 3.6 0 1 1 8.4 4.6 Z M5 2 A1.5 1.5 0 1 0 5 5 A1.5 1.5 0 1 0 5 2 Z" fill="#222" fill-rule="evenodd"/></svg><span>27 WHARFSIDE AVE, HARBORVIEW,<br>CA, 94960</span></li>
    </ul>
    <div class="divider"></div>
    <div class="stamp"></div>
    <span class="field-label" style="top:172px">From:</span>
    <div class="address-line" style="top:203px"></div>
    <div class="address-line" style="top:241px"></div>
    <div class="address-line" style="top:279px"></div>
    <span class="field-label" style="top:310px">To:</span>
    <div class="address-line" style="top:336px"></div>
    <div class="address-line" style="top:373px"></div>
    <div class="address-line" style="top:411px"></div>
  </section>
</body>
</html>
```